Brochure Design Project

Our company is TEM Bexley Fold. (no LOGO)

We are a restaurant marketing and advertising service. We market restaurants menus by producing a menu guide, distributing flyers and post cards, and also placing the restaurants menu on our website for delivery.

We make restaurants more profitable, by making their food more accessible. Marketing restaurants on search engines, websites, friendloop, vrop, zindle, and a total of 21 different marketing techniques that make restaurants more money.

Key Point: This is all done at NO COST to the restaurant.

We are looking for a design for a brochure that will be mailed as well as handed to restaurateurs.

In my attached file I am including our sales letter. The letter can stay in letter form for the inside of a tri-fold brochure or it can be part of your design.

For more information about our service, please read the attached sales letter.

Target Market(s)

Restaurant Owners and General managers

Industry/Entity Type

Advertising

Requirements
Must have
• Must look attractive and Eye-catching

```html
<!DOCTYPE html>
<html lang="en">
<head>
<meta charset="utf-8">
<title>TEM Bexley Fold – Tri-fold Brochure</title>
<link href="https://fonts.googleapis.com/css2?family=Roboto+Condensed:wght@400;700&family=Arimo:wght@400;700&family=Cabin:wght@400&display=swap" rel="stylesheet">
<style>
  :root {
    --amber: #f6a72a;
    --ink: #232323;
    --paper: #ffffff;
    --stage: #e9e6e1;
    --text-light: #f4f4f4;
    --fold-line: #8a8a8a;
  }
  * { margin: 0; padding: 0; box-sizing: border-box; }
  html, body {
    width: 1200px; height: 908px; overflow: hidden;
    background: var(--stage);
  }
  .brochure {
    position: absolute; left: 8px; top: 36px;
    width: 1184px; height: 836px;
    background: var(--ink);
    overflow: hidden;
    box-shadow: 0 4px 18px rgba(0,0,0,.25);
  }
  .brochure__art { position: absolute; inset: 0; }
  .panel-cover-bg { fill: var(--paper); }

  .cost-banner {
    position: absolute; left: 10px; top: 10px; width: 370px;
    font: 400 30px/36px 'Roboto Condensed', sans-serif;
    color: var(--paper); text-align: center;
    text-shadow: -1px -1px 0 #000, 1px -1px 0 #000, -1px 1px 0 #000, 1px 1px 0 #000, 0 2px 4px #000;
    letter-spacing: -0.5px;
  }
  .about { position: absolute; left: 29px; top: 608px; width: 318px; color: var(--text-light); }
  .about__title { font: 400 30px/36px 'Roboto Condensed', sans-serif; color: var(--paper); margin-bottom: 10px; }
  .about__text { font: 400 16px/28px 'Arimo', sans-serif; text-align: justify; letter-spacing: .3px; }

  .reach { position: absolute; left: 426px; top: 24px; width: 330px; }
  .reach__title { font: 400 30px/32px 'Roboto Condensed', sans-serif; color: var(--amber); margin-bottom: 16px; }
  .reach__text { font: 400 13.5px/25px 'Arimo', sans-serif; color: var(--text-light); text-align: justify; letter-spacing: .3px; }
  .consult {
    position: absolute; left: 429px; top: 297px; width: 320px;
    font: 400 21px/27px 'Roboto Condensed', sans-serif; color: var(--amber);
  }
  .contact {
    position: absolute; left: 432px; top: 462px; width: 300px; text-align: center;
    font: 700 16.5px/28px 'Arimo', sans-serif; color: var(--paper); letter-spacing: 1px;
  }
  .contact__lead { color: var(--amber); }

  .cover-name {
    position: absolute; left: 789px; top: 388px; width: 395px; text-align: center;
    font: 400 42px/56px 'Cabin', sans-serif; color: #111;
  }
  .cover-tab {
    position: absolute; font: 400 34px/78px 'Cabin', sans-serif; color: var(--amber);
  }
  .cover-tab--marketing { left: 830px; top: 476px; }
  .cover-tab--advertising { left: 952px; top: 566px; }
  .cover-tagline {
    position: absolute; left: 805px; top: 678px; width: 370px; text-align: center;
    font: 400 30px/37px 'Roboto Condensed', sans-serif; color: #1d1d1d;
  }
</style>
</head>
<body>
<main class="brochure">
  <svg class="brochure__art" width="1184" height="836" viewBox="0 0 1184 836">
    <defs>
      <linearGradient id="food-tones" x1="0" y1="0" x2="1" y2="1">
        <stop offset="0" stop-color="#8a5a3c"/>
        <stop offset=".5" stop-color="#c9a48a"/>
        <stop offset="1" stop-color="#b9433a"/>
      </linearGradient>
      <linearGradient id="banquet-tones" x1="0" y1="0" x2="1" y2="1">
        <stop offset="0" stop-color="#e8e2d6"/>
        <stop offset=".55" stop-color="#9a4f2c"/>
        <stop offset="1" stop-color="#2a2622"/>
      </linearGradient>
      <radialGradient id="globe-tones" cx=".4" cy=".35" r=".7">
        <stop offset="0" stop-color="#dceefa"/>
        <stop offset=".6" stop-color="#6fa6d6"/>
        <stop offset="1" stop-color="#1d4f9a"/>
      </radialGradient>
    </defs>

    <!-- cover panel -->
    <rect class="panel-cover-bg" x="789" y="0" width="395" height="836"/>
    <g role="img" aria-label="Photo of a table of restaurant dishes: roast duck, pancakes, sliced leeks and rice">
      <polygon points="973,0 1184,0 1184,158 789,300 789,190" fill="url(#banquet-tones)"/>
    </g>
    <polygon points="789,0 973,0 789,190" fill="var(--amber)"/>
    <polygon points="905,262 1184,158 1184,388" fill="var(--amber)"/>
    <polygon points="789,476 1024,476 1064,515 1024,554 789,554" fill="#111"/>
    <polygon points="948,566 1184,566 1184,644 948,644 908,605" fill="#111"/>

    <!-- inside panels -->
    <g role="img" aria-label="Photo of a smiling businesswoman in a beige suit standing before plates of restaurant food">
      <polygon points="0,0 393,0 393,490 0,178" fill="url(#food-tones)"/>
    </g>
    <polygon points="0,178 393,490 520,620 789,820 789,836 393,690 0,390" fill="var(--amber)"/>
    <line x1="393.5" y1="0" x2="393.5" y2="548" stroke="var(--fold-line)" stroke-width="1"/>

    <g role="img" aria-label="Illustration of a blue globe wrapped by binary code and arrows">
      <circle cx="580" cy="705" r="85" fill="url(#globe-tones)"/>
    </g>
  </svg>

  <p class="cost-banner">This is all done at NO COST to the restaurant.</p>

  <section class="about">
    <h2 class="about__title">ABOUT US</h2>
    <p class="about__text">TEM Bexley Fold is a restaurant marketing and advertising service that specializes in delivery. We deliver food from a variety of restaurants to people at their homes, offices or hotel rooms.</p>
  </section>

  <section class="reach">
    <h2 class="reach__title">Reach More Potential Customers!</h2>
    <p class="reach__text">Your customers are searching your business and making their decisions online more than ever. TEM Bexley Fold helps you reach thousands of potential customers on search engines and social media platforms. We manage online advertising so you don't miss out on any additional business.</p>
  </section>

  <p class="consult">To schedule a 15 min consultation that is guaranteed to NOT cost you anything and only make your restaurant money.</p>

  <p class="contact">
    <span class="contact__lead">Call Ravi Omburu Now</span><br>
    555-014-2290<br>
    or Visit<br>
    www.tembexleyfold.com
  </p>

  <h1 class="cover-name">TEM Bexley Fold</h1>
  <span class="cover-tab cover-tab--marketing">MARKETING</span>
  <span class="cover-tab cover-tab--advertising">ADVERTISING</span>
  <p class="cover-tagline">We make Restaurants more profitable, by Making their food more accessible!</p>
</main>
</body>
</html>
```